Need business card design for a confectionery company specializing in chocolates. Would like to see designs that use chocolate brown background and lime green wording and logo. Logo preferably chocolate-related.

Target Market(s)

Corporate, Gifts & Occasions, Hotels, Supermarkets, Parties, Events, Weddings

Industry/Entity Type

Food Production

Contact Information for Business Card

Velbrook Confectionery (company name on front of card in lime green)
with words beneath company name saying "chocolates for every occassion" (in lime green in lower case)

Font styles to use
Script

Colors
acd037

Requirements
Must have
• Front of card: Brown background
• Back of card: White background
• Email address on back of card: Info@velbrook.example.zw
• Cellphone number on back of card: 0771 352 690, 0773 214 587
• Address on back of card: 12 Marula Lane, Eastvale, Harare
• ALL WRITING ON BACK OF CARD IN BLACK

```html
<!DOCTYPE html>
<html lang="en">
<head>
<meta charset="utf-8">
<title>Velbrook Confectionery – Business Card</title>
<link rel="stylesheet" href="https://fonts.googleapis.com/css2?family=Chewy&family=Dancing+Script:wght@500&family=Delius+Swash+Caps&family=Questrial&display=block">
<style>
  :root {
    --page-bg: #e9e6e1;
    --card-brown: #a65a2e;
    --card-brown-dark: #8f4a22;
    --card-brown-light: #c07a45;
    --lime: #9bdc3f;
    --stripe-slate: #34505e;
    --stripe-red: #a01818;
    --card-white: #ffffff;
    --ink: #111111;
    --shadow: rgba(0, 0, 0, 0.35);
  }
  * { box-sizing: border-box; margin: 0; padding: 0; }
  html, body {
    width: 1200px;
    height: 923px;
    overflow: hidden;
    background: var(--page-bg);
  }
  .canvas {
    position: relative;
    width: 1200px;
    height: 923px;
  }
  .card {
    position: absolute;
    left: 358px;
    width: 484px;
    height: 275px;
    box-shadow: 6px 8px 14px var(--shadow);
    overflow: hidden;
  }

  /* Front */
  .card-front {
    top: 158px;
    background: var(--card-brown);
  }
  .front-photo {
    position: absolute;
    inset: 0 0 8px 0;
    background:
      radial-gradient(ellipse 30% 35% at 40% 25%, var(--card-brown-light), transparent 70%),
      radial-gradient(ellipse 40% 30% at 20% 80%, var(--card-brown-dark), transparent 70%),
      linear-gradient(180deg, var(--card-brown) 0%, var(--card-brown-dark) 100%);
    opacity: 0.9;
  }
  .front-brand {
    position: absolute;
    left: 0;
    right: 0;
    top: 108px;
    text-align: center;
    color: var(--lime);
  }
  .company-name {
    display: inline-block;
    font-family: "Chewy", "Comic Sans MS", cursive;
    font-weight: 400;
    font-size: 25px;
    letter-spacing: 1.5px;
    text-transform: uppercase;
    padding-bottom: 1px;
    border-bottom: 1.5px solid var(--lime);
    line-height: 1.1;
  }
  .tagline {
    font-family: "Dancing Script", cursive;
    font-size: 20px;
    letter-spacing: 1px;
    margin-top: 3px;
  }
  .front-stripe {
    position: absolute;
    left: 0; right: 0; bottom: 0;
    height: 8px;
    display: flex;
  }
  .front-stripe .stripe-slate { flex: 1; background: var(--stripe-slate); }
  .front-stripe .stripe-red { flex: 1; background: var(--stripe-red); }

  /* Back */
  .card-back {
    top: 490px;
    height: 274px;
    width: 480px;
    background: var(--card-white);
    color: var(--ink);
  }
  .holder-name {
    position: absolute;
    left: 0; right: 0;
    top: 28px;
    text-align: center;
    font-family: "Delius Swash Caps", cursive;
    font-weight: 400;
    font-size: 34px;
    letter-spacing: 2px;
  }
  .contact-rule {
    position: absolute;
    left: 103px;
    top: 113px;
    width: 1.5px;
    height: 110px;
    background: var(--ink);
  }
  .contact-row {
    position: absolute;
    left: 78px;
    display: flex;
    align-items: center;
    font-family: "Questrial", sans-serif;
    font-size: 13.5px;
    letter-spacing: 1.2px;
    white-space: nowrap;
  }
  .contact-row svg { width: 18px; height: 18px; margin-right: 16px; fill: var(--ink); flex: none; }
  .contact-phone { top: 113px; letter-spacing: 2.4px; font-size: 14px; }
  .contact-phone .phone-divider { margin: 0 8px; letter-spacing: 0; }
  .contact-email { top: 157px; }
  .contact-address { top: 203px; }
</style>
</head>
<body>
<main class="canvas">

  <section class="card card-front">
    <div class="front-photo" role="img" aria-label="Softly blurred photograph of assorted chocolates under a warm brown tint"></div>
    <div class="front-brand">
      <h1 class="company-name">Velbrook Confectionery</h1>
      <p class="tagline">Chocolates for every occassion</p>
    </div>
    <div class="front-stripe">
      <span class="stripe-slate"></span>
      <span class="stripe-red"></span>
    </div>
  </section>

  <section class="card card-back">
    <h2 class="holder-name">Rutendo Zhou</h2>
    <span class="contact-rule"></span>

    <p class="contact-row contact-phone">
      <svg viewBox="0 0 24 24" aria-hidden="true"><path d="M6.6 10.8c1.4 2.8 3.8 5.1 6.6 6.6l2.2-2.2c.3-.3.7-.4 1-.2 1.1.4 2.3.6 3.6.6.6 0 1 .4 1 1V20c0 .6-.4 1-1 1C10.6 21 3 13.4 3 4c0-.6.4-1 1-1h3.5c.6 0 1 .4 1 1 0 1.3.2 2.5.6 3.6.1.3 0 .7-.2 1z"/></svg>
      0771 352 690<span class="phone-divider">/</span>0773 214 587
    </p>

    <p class="contact-row contact-email">
      <svg viewBox="0 0 24 24" aria-hidden="true"><path d="M2 5h20v14H2z M4 7v.5l8 5.5 8-5.5V7l-8 5.5z" fill-rule="evenodd"/></svg>
      Info@velbrook.example.zw
    </p>

    <p class="contact-row contact-address">
      <svg viewBox="0 0 24 24" aria-hidden="true"><path d="M12 2a7 7 0 0 0-7 7c0 5.2 7 13 7 13s7-7.8 7-13a7 7 0 0 0-7-7zm0 9.5A2.5 2.5 0 1 1 12 6.5a2.5 2.5 0 0 1 0 5z"/></svg>
      12 Marula Lane, Eastvale, Harare
    </p>
  </section>

</main>
</body>
</html>
```